Jewelery Website

Please visit: http://www.lucastorvi.com/dev/wpnew/

Target Market(s)

Women between 25 and 44 years old

Number of Pages Required

5+ page

Font styles to use
Sans Serif
Script
Other font styles liked:
• Futura

Colors

Designer to choose colors to be used in the design.

```html
<!DOCTYPE html>
<html lang="en">
<head>
<meta charset="utf-8">
<title>Lucas Torvi Pearls – Jewellery</title>
<link href="https://fonts.googleapis.com/css2?family=Playfair+Display:wght@400;700;900&family=Raleway:wght@400;600;700&display=swap" rel="stylesheet">
<style>
:root{
  --backdrop:#94979c;
  --cream:#f8f5ef;
  --white:#ffffff;
  --ink:#111111;
  --ink-soft:#555555;
  --muted:#9a9a9a;
  --tan:#a88d6c;
  --ghost:#ebe5dc;
  --tile:#f6f2ea;
  --line:#c9b59c;
  --serif:'Playfair Display', Georgia, serif;
  --sans:'Raleway', Arial, sans-serif;
}
*{margin:0;padding:0;box-sizing:border-box}
html,body{width:960px;height:1200px;overflow:hidden;background:var(--backdrop)}
.stage{position:relative;width:1200px;height:1500px;transform:scale(.8);transform-origin:0 0;font-family:var(--sans);color:var(--ink)}
.abs{position:absolute}
.page-top{left:273px;top:0;width:607px;height:1125px;background:var(--cream)}
.page-bottom{left:273px;top:1125px;width:602px;height:375px;background:var(--cream)}

/* header */
.brand{left:290px;top:18px;display:flex;align-items:center;gap:6px}
.brand-mark{width:14px;height:14px;background:var(--ink)}
.brand-name{font-family:var(--sans);font-weight:700;font-size:10px;letter-spacing:1.5px;color:var(--ink);line-height:1.1}
.nav{left:490px;top:18px;display:flex;gap:15px;font-size:5px;font-weight:700;letter-spacing:.5px}
.tools{left:822px;top:16px;display:flex;gap:7px}

/* hero */
.hero{left:289px;top:69px;width:575px;height:271px;background:linear-gradient(100deg,#0d0d0e 0%,#2b2c2f 55%,#1c1e22 100%)}
.hero-photo{left:40px;top:0;width:200px;height:271px;background:radial-gradient(ellipse at center,#4a5060 0%,#2a2d35 60%,transparent 80%)}
.hero-title{left:200px;top:100px;width:405px;text-align:center;font-family:var(--serif);font-weight:900;font-size:26px;color:var(--white);letter-spacing:-.3px}
.hero-sub{left:200px;top:134px;width:405px;text-align:center;font-size:10px;color:#e8e8e8;letter-spacing:.3px}
.btn-tan{background:var(--tan);color:var(--white);font-size:4.5px;font-weight:700;letter-spacing:.6px;text-align:center}
.hero-btn{left:381px;top:159px;width:44px;height:12px;line-height:12px}

/* intro */
.intro-photo{left:390px;top:388px;width:142px;height:92px;background:radial-gradient(ellipse at 50% 60%,#e7d3a5 0%,#d8d8d8 45%,transparent 72%)}
.intro-title{left:390px;top:488px;font-family:var(--serif);font-weight:700;font-size:12.5px}
.intro-text{left:390px;top:510px;width:226px;font-size:4.6px;line-height:1.4;color:var(--ink-soft)}
.btn-outline{border:1px solid var(--line);color:var(--tan);font-size:4.5px;letter-spacing:.5px;text-align:center;background:transparent}
.intro-btn{left:390px;top:535px;width:45px;height:13px;line-height:11px}
.feature{left:622px;width:141px;height:52px;background:var(--white);display:flex;align-items:center;padding-left:15px;gap:10px}
.feature-title{font-family:var(--serif);font-weight:700;font-size:11px;line-height:1}
.feature-sub{font-size:4px;color:var(--muted);margin-top:2px}

/* product sections */
.panel-white{background:var(--white)}
.products-a{left:289px;top:623px;width:575px;height:392px}
.products-b{left:285px;top:1130px;width:575px;height:227px}
.section-rule{width:1.5px;height:48px;background:var(--tan)}
.section-ghost{font-family:var(--serif);font-weight:900;font-size:31px;color:var(--ghost);letter-spacing:.5px;line-height:1}
.tabs{left:638px;top:655px;display:flex;gap:6px}
.tab{height:10px;line-height:8px;font-size:4px;font-weight:700;letter-spacing:.5px;padding:0 6px;border:1px solid var(--line);color:var(--ink-soft)}
.tab.is-active{background:var(--tan);border-color:var(--tan);color:var(--white)}
.card{width:86px}
.card-photo{position:relative;width:86px;height:96px;background:var(--tile)}
.card-photo .shape{position:absolute;left:18px;top:14px;width:50px;height:70px;border-radius:40%;background:radial-gradient(ellipse,#d7b56a 0%,#e9d9b4 55%,transparent 75%)}
.card-photo .shape.silver{background:radial-gradient(ellipse,#c9c3c6 0%,#e4dfe2 55%,transparent 75%)}
.card-photo .shape.rose{background:radial-gradient(ellipse,#d9b2a8 0%,#ecdcd6 55%,transparent 75%)}
.card-photo .shape.blue{background:radial-gradient(ellipse,#6fa9c8 0%,#e6d3c2 45%,transparent 75%)}
.tag{position:absolute;top:3px;font-size:4px;font-weight:700}
.tag.new{left:3px}.tag.sale{right:3px}
.card-name{font-size:4.5px;color:var(--muted);margin-top:6px}
.card-price{font-size:4.8px;font-weight:700;margin-top:4px}
.card-price s{color:var(--muted);font-weight:400;margin-left:3px}
.more-btn{left:541px;top:974px;width:72px;height:11px;line-height:9px}
.arrows{font-family:var(--sans);font-size:14px;color:#444;display:flex;align-items:center;gap:2px}
.arrows .slash{font-size:20px;color:#ccc;transform:rotate(-5deg)}

/* bands */
.band{background:radial-gradient(ellipse at 20% 30%,#2b2b2b 0%,#0b0b0b 55%,#050505 100%)}
.band-designs{left:289px;top:1015px;width:575px;height:107px}
.band-title{left:289px;top:1048px;width:575px;text-align:center;font-family:var(--serif);font-weight:700;font-size:13px;color:var(--white)}
.band-title em{font-style:normal;color:var(--tan)}
.band-sub{left:289px;top:1067px;width:575px;text-align:center;font-size:6px;color:#e5e5e5}
.band-news{left:284px;top:1357px;width:575px;height:80px}
.news-text{left:385px;top:1387px;font-family:var(--serif);font-weight:700;font-size:8.5px;color:var(--white);line-height:1.25;letter-spacing:.3px}
.news-input{left:553px;top:1388px;width:147px;height:15px;background:var(--white);font-size:4.5px;color:var(--muted);padding:5px 4px}
.news-btn{left:704px;top:1388px;width:54px;height:15px;line-height:15px}
</style>
</head>
<body>
<div class="stage">
  <div class="abs page-top"></div>
  <div class="abs page-bottom"></div>

  <header>
    <div class="abs brand">
      <span class="brand-mark"></span>
      <span class="brand-name">LUCAS TORVI<br>PEARLS</span>
    </div>
    <nav class="abs nav">
      <span>BRACELETS</span><span>CHAIN</span><span>RINGS</span><span>ANKLET</span><span>NECKLACES</span><span>MORE</span>
    </nav>
    <div class="abs tools">
      <svg width="9" height="9" viewBox="0 0 10 10" fill="none" stroke="#111" stroke-width="1.2"><circle cx="4.2" cy="4.2" r="3"/><path d="M6.5 6.5L9 9"/></svg>
      <svg width="9" height="9" viewBox="0 0 10 10" fill="none" stroke="#111" stroke-width="1.1"><circle cx="5" cy="3" r="2"/><path d="M1.5 9.5c0-2.2 1.6-3.5 3.5-3.5s3.5 1.3 3.5 3.5z"/></svg>
      <svg width="10" height="10" viewBox="0 0 10 10" fill="none" stroke="#111" stroke-width="1.1"><rect x="1.5" y="3.5" width="6.5" height="5.5"/><path d="M3 3.5V2.2a1.7 1.7 0 013.4 0v1.3"/><circle cx="8.5" cy="1.8" r="1.3" fill="#a88d6c" stroke="none"/></svg>
    </div>
  </header>

  <section class="abs hero">
    <div class="abs hero-photo" role="img" aria-label="Diamond and sapphire necklace, earrings, ring and bracelet set"></div>
    <h1 class="abs hero-title">EXPLORE OUR FASHION</h1>
    <p class="abs hero-sub">Traditional&nbsp; Real Gold Jewellery</p>
    <div class="abs btn-tan hero-btn">SHOP NOW</div>
  </section>

  <section>
    <div class="abs intro-photo" role="img" aria-label="Pair of diamond rings in white and yellow gold"></div>
    <h2 class="abs intro-title">Your Diamond &amp; Jewellery</h2>
    <p class="abs intro-text">Every piece is crafted by hand with care and is made to be worn each day. Our diamonds are chosen for light and fire, set in real gold that keeps its shine for years to come, and sold with full certificates.</p>
    <div class="abs btn-outline intro-btn">READ MORE</div>

    <div class="abs feature" style="top:392px">
      <svg width="26" height="18" viewBox="0 0 26 18" fill="none" stroke="#111" stroke-width="1.3"><path d="M1 2h15v11H1z"/><path d="M16 6h5l4 4v3h-9"/><circle cx="6" cy="14.5" r="2.2" fill="#fff"/><circle cx="20" cy="14.5" r="2.2" fill="#fff"/></svg>
      <div><div class="feature-title">Free Delivery</div><div class="feature-sub">For Orders Over $100</div></div>
    </div>
    <div class="abs feature" style="top:453px">
      <svg width="26" height="24" viewBox="0 0 26 24" fill="none" stroke="#111" stroke-width="1.3"><path d="M5 13V10a8 8 0 0116 0v3"/><rect x="3" y="12" width="4" height="7" rx="1.5"/><rect x="19" y="12" width="4" height="7" rx="1.5"/><path d="M21 19c0 3-3 4-7 4"/></svg>
      <div><div class="feature-title">Best Support</div><div class="feature-sub">Hours 9am - 11pm</div></div>
    </div>
    <div class="abs feature" style="top:514px">
      <svg width="26" height="24" viewBox="0 0 26 24" fill="none" stroke="#111" stroke-width="1.3"><rect x="2" y="10" width="5" height="12"/><path d="M7 11l5-8c2 0 3 1 2.5 3L13.5 10h7a2 2 0 012 2.4l-1.8 7.6a2 2 0 01-2 1.5H7"/></svg>
      <div><div class="feature-title">Special Offers</div><div class="feature-sub">50% Off On Diamonds</div></div>
    </div>
  </section>

  <section class="abs panel-white products-a"></section>
  <div class="abs section-rule" style="left:386px;top:623px"></div>
  <h2 class="abs section-ghost" style="left:390px;top:643px">PRODUCTS</h2>
  <div class="abs tabs">
    <span class="tab is-active">BRACELETS</span><span class="tab">NOSE-JEWEL</span><span class="tab">ANKLET</span>
  </div>

  <article class="abs card" style="left:390px;top:693px"><div class="card-photo" role="img" aria-label="Rose gold ear chains"><span class="shape rose"></span><span class="tag new">NEW</span></div><div class="card-name">Habitasse Platea Dictumst</div><div class="card-price">$90.00<s>$100.00</s></div></article>
  <article class="abs card" style="left:486px;top:693px"><div class="card-photo" role="img" aria-label="Gold jhumka earrings"><span class="shape"></span><span class="tag new">NEW</span></div><div class="card-name">Arcu Vitae Imperdiet</div><div class="card-price">$750.00</div></article>
  <article class="abs card" style="left:582px;top:693px"><div class="card-photo" role="img" aria-label="Blue topaz pendant necklace"><span class="shape blue"></span><span class="tag new">NEW</span></div><div class="card-name">Suspendisse Massa Nulla</div><div class="card-price">$110.00</div></article>
  <article class="abs card" style="left:677px;top:693px"><div class="card-photo" role="img" aria-label="Diamond drop earrings"><span class="shape silver"></span><span class="tag new">NEW</span><span class="tag sale">ON SALE!</span></div><div class="card-name">Justo Neque Commodo Nisi</div><div class="card-price">$250.00</div></article>

  <article class="abs card" style="left:390px;top:832px"><div class="card-photo" role="img" aria-label="Gold floral bracelet"><span class="shape"></span><span class="tag new">NEW</span></div><div class="card-name">Tellus Eu Volutpat Varius</div><div class="card-price">$45.00</div></article>
  <article class="abs card" style="left:486px;top:832px"><div class="card-photo" role="img" aria-label="Gold tassel drop earrings"><span class="shape"></span><span class="tag new">NEW</span><span class="tag sale">ON SALE!</span></div><div class="card-name">Varius Neque At Enim</div><div class="card-price">$16.00<s>$30.00</s></div></article>
  <article class="abs card" style="left:582px;top:832px"><div class="card-photo" role="img" aria-label="Gold chandelier earrings"><span class="shape"></span><span class="tag new">NEW</span></div><div class="card-name">Varius Neque At Enim</div><div class="card-price">$98.00<s>$120.00</s></div></article>
  <article class="abs card" style="left:677px;top:832px"><div class="card-photo" role="img" aria-label="Rose gold diamond ring"><span class="shape rose"></span><span class="tag new">NEW</span></div><div class="card-name">Phasellus Sit Amet Urna</div><div class="card-price">$250.00</div></article>

  <div class="abs btn-outline more-btn">VIEW MORE PRODUCTS</div>

  <section class="abs band band-designs" role="img" aria-label="Dark textured stone background"></section>
  <h2 class="abs band-title">5000+ Designs From <em>Diamond &amp; Gold Jewellery</em> Collection.</h2>
  <p class="abs band-sub">Buy Jewellery Online For Best Prices!</p>

  <section class="abs panel-white products-b"></section>
  <div class="abs section-rule" style="left:381px;top:1130px"></div>
  <h2 class="abs section-ghost" style="left:385px;top:1150px">PRODUCTS</h2>
  <div class="abs arrows" style="left:724px;top:1152px"><span>&lt;</span><span class="slash">/</span><span>&gt;</span></div>

  <article class="abs card" style="left:385px;top:1199px"><div class="card-photo" role="img" aria-label="Gold beaded necklace with pendant"><span class="shape"></span><span class="tag new">NEW</span><span class="tag sale">ON SALE!</span></div><div class="card-name">Aliquam Erat Volutpat</div><div class="card-price">$38.00<s>$70.00</s></div></article>
  <article class="abs card" style="left:481px;top:1199px"><div class="card-photo" role="img" aria-label="Gold chain bracelet with heart"><span class="shape"></span><span class="tag new">NEW</span></div><div class="card-name">Donec Semper Tristique</div><div class="card-price">$135.00</div></article>
  <article class="abs card" style="left:577px;top:1199px"><div class="card-photo" role="img" aria-label="Gold teardrop pendant"><span class="shape"></span><span class="tag new">NEW</span></div><div class="card-name">Integer Tempor Lacus Eget</div><div class="card-price">$40.00<s>$50.00</s></div></article>
  <article class="abs card" style="left:672px;top:1199px"><div class="card-photo" role="img" aria-label="Gold beaded necklace with pendant"><span class="shape"></span><span class="tag new">NEW</span></div><div class="card-name">Nullam Mollis Dolor Ac</div><div class="card-price">$80.00</div></article>

  <section class="abs band band-news"></section>
  <p class="abs news-text">SIGN UP FOR<br>EMAIL AND GET 20$ OFF</p>
  <div class="abs news-input">Your email address</div>
  <div class="abs btn-tan news-btn">SUBSCRIBE NOW</div>

  <div class="abs section-rule" style="left:381px;top:1437px;height:63px"></div>
  <h2 class="abs section-ghost" style="left:385px;top:1458px">PEOPLE SAYS</h2>
  <div class="abs arrows" style="left:719px;top:1461px"><span>&lt;</span><span class="slash">/</span><span>&gt;</span></div>
</div>
</body>
</html>
```